8" x 11" One Page Flyer for Fence Installation Company

We are looking to promote our business with a new flyer that would be handed out in person to people or put at their mailbox/door at their homes. The flyer needs to be creative and attention-grabbing. I have attached some of our previous flyers and our website information. Do not call or email regarding the flyer. We want the flyer to look professional but also friendly. One page, NOT folded. You can use images from our website at www.MyBraxtonYard.com or our Facebook page at www.Facebook.com/HollowbrookRailsBKT. We are flexible with what photos you can use but there must be photos of OUR fences on the flyer. More photos specifically can also be provided. Colors need to be suitable for a flyer printed on canary yellow in color paper OR white paper.

Target Market(s)

Homeowners that need a new fence

Industry/Entity Type

Construction

Font styles to use
Sans Serif
Other font styles liked:
• HD Colton

Colors
0054AA
0677BA
7BADD7
CADEEF
E8F1F8
0094D4
00A9DD
6FCCEA
C7EBF8
E9F6FB

Requirements
Must have
• Our fence photos - mostly wood fence photos (different designs), SIZE SHOULD BE LETTER SIZE 8" x 11"
Nice to have
• A nice bible verse featured at the bottom of the flyer.
Should not have
• DO NOT COPY THE WEBSITE FORMAT, I WANT SOMETHING UNIQUE. Other people's fence photos, they must all come from our website or facebook page

```html
<!DOCTYPE html>
<html lang="en">
<head>
<meta charset="utf-8">
<title>Braxton Yard Fence Flyer</title>
<link rel="stylesheet" href="https://fonts.googleapis.com/css2?family=Montserrat:wght@600;700;800&family=Exo+2:wght@600;700&family=Oswald:wght@400;500&display=swap">
<style>
:root{
  --page:#f1ebe3;
  --blue-deep:#0054aa;
  --blue-mid:#3d8fd0;
  --blue-light:#8ebbe3;
  --brown:#6e5a4a;
  --orange:#e4a452;
  --orange-text:#f2a93b;
  --wood-a:#b97a3a;
  --wood-b:#dba565;
  --ink:#111111;
  --white:#ffffff;
  --paper:#f4f4f4;
}
*{margin:0;padding:0;box-sizing:border-box}
html,body{width:1200px;height:2400px;overflow:hidden;background:var(--page)}
.flyer{position:absolute;left:0;top:375px;width:1200px;height:1650px;overflow:hidden;background:var(--paper);font-family:"Montserrat",sans-serif}
.abs{position:absolute;white-space:nowrap}

.hero-photo{left:0;top:0;width:1200px;height:470px;background:linear-gradient(180deg,#6a9ad6 0%,#a46d52 38%,#c9a878 70%,#8c7a55 100%)}
.blue-field{left:0;top:458px;width:1200px;height:735px;background:linear-gradient(90deg,var(--blue-mid) 0%,#5ea2d9 55%,var(--blue-light) 100%)}
.footer-band{left:0;top:1437px;width:1200px;height:213px;background:var(--brown)}

.header-card{left:0;top:0;width:500px;height:213px}
.brand{left:61px;top:70px;display:flex;align-items:center;gap:14px}
.brand-dot{width:30px;height:30px;border-radius:50%;background:var(--orange)}
.brand-name{font-weight:800;font-size:32px;color:var(--blue-deep);line-height:1}
.brand-phone{left:105px;top:112px;font-weight:800;font-size:30px;color:var(--ink)}
.brand-tagline{left:105px;top:152px;font-weight:700;font-size:11px;color:var(--ink)}

.why-banner{left:0;top:347px;width:680px;height:134px}
.why-title{left:61px;top:355px;font-weight:800;font-size:47px;color:var(--white)}
.why-sub{left:61px;top:416px;font-weight:700;font-size:19px;line-height:25px;color:var(--ink)}

.hex{top:254px;width:233px;height:268px}
.hex-a{left:626px}.hex-b{left:909px}

.checklist{left:79px;top:517px;list-style:none}
.checklist li{display:flex;align-items:center;gap:22px;height:50px;font-family:"Exo 2",sans-serif;font-weight:600;font-size:26px;color:var(--white)}

.where-title{left:674px;top:544px;font-weight:800;font-size:50px;line-height:60px;color:var(--ink)}
.map-frame{left:722px;top:621px;width:490px;height:236px;border:8px solid var(--white);border-right:none;border-radius:22px 0 0 22px;background:linear-gradient(135deg,#eef0ee,#dfe3e0);overflow:hidden}

.estimates-banner{left:0;top:828px;width:560px;height:86px}
.estimates-text{left:61px;top:842px;font-weight:800;font-size:44px;color:var(--ink)}
.estimates-text .lead{color:var(--white)}

.open-line{left:61px;top:940px;font-weight:700;font-size:25px;color:var(--ink)}
.hl{color:var(--orange-text)}
.calendar{left:60px;top:980px;width:66px;height:66px;border-radius:50%;background:var(--brown);display:flex;align-items:center;justify-content:center}
.hours{top:986px}
.hours .day{font-weight:700;font-size:31px;color:var(--white);line-height:40px}
.hours .time{font-weight:700;font-size:20px;color:var(--ink);line-height:24px}
.hours-a{left:147px}.hours-b{left:445px}

.showroom-box{left:627px;top:885px;width:573px;height:106px;background:var(--brown);border-radius:14px 0 0 14px;padding:16px 0 0 15px;font-family:"Exo 2",sans-serif;font-weight:700;color:var(--white)}
.showroom-box .line1{font-size:26px;line-height:36px}
.showroom-box .line2{font-size:22px;line-height:38px}
.showroom-box .big{font-size:32px;color:var(--orange-text)}

.gate-line{left:680px;top:1034px;font-family:"Oswald",sans-serif;font-weight:500;font-size:33px;color:var(--white);line-height:44px}
.gate-line .tag{background:var(--white);color:var(--ink);padding:0 4px}

.paper-strip{left:0;top:1186px;width:1200px;height:251px;background:linear-gradient(180deg,#ffffff,#ededed)}
.card{top:1114px;width:214px;height:205px;background:var(--white);padding:9px;border-radius:6px;box-shadow:0 2px 6px rgba(0,0,0,.18)}
.card .photo{width:100%;height:100%}
.card-1{left:63px}.card-2{left:350px}.card-3{left:637px}.card-4{left:924px}
.caption{top:1340px;width:260px;text-align:center;font-family:"Oswald",sans-serif;font-weight:400;font-size:25px;line-height:32px;color:var(--ink)}
.cap-1{left:40px}.cap-2{left:327px;top:1322px;line-height:29px}.cap-3{left:614px}.cap-4{left:901px}

.verse{left:112px;top:1396px;width:954px;height:70px;background:var(--orange);border:5px solid var(--white);border-radius:22px;display:flex;align-items:center;justify-content:center;gap:12px;font-family:"Oswald",sans-serif;color:var(--white);z-index:2}
.verse .quote{font-size:46px;font-weight:500}
.verse .ref{font-size:32px;color:var(--ink)}

.contact{display:flex;align-items:center;gap:16px;color:var(--white);font-weight:700}
.c-phone{left:63px;top:1500px;font-size:40px}
.c-addr{left:63px;top:1557px;font-size:26px}
.c-web{left:660px;top:1503px;font-size:30px}
.c-mail{left:660px;top:1557px;font-size:29px}
</style>
</head>
<body>
<main class="flyer">

  <div class="abs hero-photo" role="img" aria-label="Photo of a new wooden three-rail fence running beside a brick house"></div>

  <svg class="abs header-card" viewBox="0 0 500 213" aria-hidden="true">
    <polygon points="0,0 500,0 462,213 0,213" fill="var(--blue-deep)"/>
    <polygon points="0,0 488,0 452,203 0,203" fill="var(--white)"/>
  </svg>
  <div class="abs brand"><span class="brand-dot"></span><span class="brand-name">Braxton Yard Fence</span></div>
  <div class="abs brand-phone">555-310-4471</div>
  <div class="abs brand-tagline">“Because Good Fences Make Good Neighbors”</div>

  <div class="abs blue-field"></div>

  <svg class="abs why-banner" viewBox="0 0 680 134" aria-hidden="true">
    <defs>
      <linearGradient id="wood" x1="0" y1="0" x2="1" y2="1">
        <stop offset="0" stop-color="var(--wood-a)"/>
        <stop offset="0.5" stop-color="var(--wood-b)"/>
        <stop offset="1" stop-color="var(--wood-a)"/>
      </linearGradient>
    </defs>
    <polygon points="0,0 620,0 570,52 615,52 520,134 0,134" fill="url(#wood)"/>
  </svg>
  <h1 class="abs why-title">WHY CHOOSE US?</h1>
  <p class="abs why-sub">Beautiful, Professionally Installed Fences<br>at Affordable Prices!</p>

  <svg class="abs hex hex-a" viewBox="0 0 233 268" role="img" aria-label="Photo of a black aluminium picket fence on a lawn">
    <polygon points="116.5,5 228,69 228,199 116.5,263 5,199 5,69" fill="#5f7d4a" stroke="var(--white)" stroke-width="10"/>
  </svg>
  <svg class="abs hex hex-b" viewBox="0 0 233 268" role="img" aria-label="Photo of a tall wooden shadowbox privacy fence">
    <polygon points="116.5,5 228,69 228,199 116.5,263 5,199 5,69" fill="#c9b58c" stroke="var(--white)" stroke-width="10"/>
  </svg>

  <ul class="abs checklist">
    <li><svg width="26" height="26" viewBox="0 0 26 26"><path d="M22 9 A11 11 0 1 1 17 3" fill="none" stroke="#fff" stroke-width="2"/><path d="M7 13 l5 5 L24 5" fill="none" stroke="#fff" stroke-width="2"/></svg>Professional Installation.</li>
    <li><svg width="26" height="26" viewBox="0 0 26 26"><path d="M22 9 A11 11 0 1 1 17 3" fill="none" stroke="#fff" stroke-width="2"/><path d="M7 13 l5 5 L24 5" fill="none" stroke="#fff" stroke-width="2"/></svg>Concrete in Every Post.</li>
    <li><svg width="26" height="26" viewBox="0 0 26 26"><path d="M22 9 A11 11 0 1 1 17 3" fill="none" stroke="#fff" stroke-width="2"/><path d="M7 13 l5 5 L24 5" fill="none" stroke="#fff" stroke-width="2"/></svg>HOA Submission Assistance.</li>
    <li><svg width="26" height="26" viewBox="0 0 26 26"><path d="M22 9 A11 11 0 1 1 17 3" fill="none" stroke="#fff" stroke-width="2"/><path d="M7 13 l5 5 L24 5" fill="none" stroke="#fff" stroke-width="2"/></svg>Lifetime Workmanship Warranty.</li>
    <li><svg width="26" height="26" viewBox="0 0 26 26"><path d="M22 9 A11 11 0 1 1 17 3" fill="none" stroke="#fff" stroke-width="2"/><path d="M7 13 l5 5 L24 5" fill="none" stroke="#fff" stroke-width="2"/></svg>Experienced Installation Teams.</li>
    <li><svg width="26" height="26" viewBox="0 0 26 26"><path d="M22 9 A11 11 0 1 1 17 3" fill="none" stroke="#fff" stroke-width="2"/><path d="M7 13 l5 5 L24 5" fill="none" stroke="#fff" stroke-width="2"/></svg>Quality Workmanship &amp; Materials.</li>
  </ul>

  <h2 class="abs where-title">Where Are We ?</h2>
  <div class="abs map-frame" role="img" aria-label="Street map showing the showroom location"></div>

  <svg class="abs estimates-banner" viewBox="0 0 560 86" aria-hidden="true">
    <path d="M0,6 L520,0 L500,14 L560,10 L515,30 L540,40 L505,52 L545,62 L500,72 L520,84 L0,86 Z" fill="var(--orange)"/>
  </svg>
  <div class="abs estimates-text"><span class="lead">Free</span> Estimates!</div>

  <p class="abs open-line">Our <span class="hl">Indoor Showroom</span> and <span class="hl">Office</span> is Open</p>
  <div class="abs calendar">
    <svg width="34" height="32" viewBox="0 0 34 32" aria-hidden="true"><rect x="1" y="4" width="32" height="27" rx="3" fill="#fff"/><rect x="1" y="4" width="32" height="8" rx="3" fill="#e05a4a"/><g fill="#c9c9c9"><rect x="5" y="15" width="5" height="4"/><rect x="12" y="15" width="5" height="4"/><rect x="19" y="15" width="5" height="4"/><rect x="26" y="15" width="4" height="4"/><rect x="5" y="22" width="5" height="4"/><rect x="12" y="22" width="5" height="4"/><rect x="19" y="22" width="5" height="4"/></g></svg>
  </div>
  <div class="abs hours hours-a"><div class="day">Monday -Thurs</div><div class="time">9AM - 3PM</div></div>
  <div class="abs hours hours-b"><div class="day">Friday</div><div class="time">9AM - 1PM</div></div>

  <div class="abs showroom-box">
    <div class="line1">Visit Our <span class="hl">Indoor</span> &amp; <span class="hl">Outdoor Showroom!</span></div>
    <div class="line2">Our Outdoor Showroom Is Open <span class="big">24/7</span></div>
  </div>

  <p class="abs gate-line"><span class="tag">FREE</span> Gate Adjustments for <span class="tag">LIFE</span></p>

  <div class="abs paper-strip"></div>

  <figure class="abs card card-1"><div class="photo" role="img" aria-label="Photo of a wooden top cap privacy fence gate" style="background:linear-gradient(180deg,#a9c3dc,#b4a27e 35%,#8f7d5a)"></div></figure>
  <figure class="abs card card-2"><div class="photo" role="img" aria-label="Photo of a flat top black standard picket fence" style="background:linear-gradient(180deg,#9fb7cf,#4e6b3c 45%,#6d8f4a)"></div></figure>
  <figure class="abs card card-3"><div class="photo" role="img" aria-label="Photo of a dog ear wooden privacy fence" style="background:linear-gradient(90deg,#6e5a44,#d6b98c 30%,#c9a878)"></div></figure>
  <figure class="abs card card-4"><div class="photo" role="img" aria-label="Photo of a split rail fence with wire mesh" style="background:linear-gradient(180deg,#a35c48,#b9a377 45%,#7d8d52)"></div></figure>

  <p class="abs caption cap-1">Top Cap Privacy Fence</p>
  <p class="abs caption cap-2">Flat Top Black<br>Standard Picket</p>
  <p class="abs caption cap-3">Dog Ear Privacy Fence</p>
  <p class="abs caption cap-4">Rail Split Rail Wire</p>

  <div class="abs footer-band"></div>

  <div class="abs verse"><span class="quote">‘ For we walk by faith, not by sight ’. _</span><span class="ref">Corinthians 5:7</span></div>

  <div class="abs contact c-phone">
    <svg width="36" height="36" viewBox="0 0 36 36" aria-hidden="true"><circle cx="18" cy="18" r="17" fill="#fff"/><path d="M12 9 l4 0 l2 6 l-3 2 a14 14 0 0 0 6 6 l2 -3 l6 2 l0 4 a3 3 0 0 1 -3 3 a18 18 0 0 1 -17 -17 a3 3 0 0 1 3 -3z" fill="var(--brown)"/></svg>
    <span>555-<span class="hl">310</span>-4471</span>
  </div>
  <div class="abs contact c-addr">
    <svg width="30" height="34" viewBox="0 0 30 34" aria-hidden="true"><path d="M15 1 a10 10 0 0 1 10 10 c0 7 -10 15 -10 15 s-10 -8 -10 -15 a10 10 0 0 1 10 -10z" fill="#fff"/><circle cx="15" cy="11" r="4" fill="var(--brown)"/><ellipse cx="15" cy="30" rx="13" ry="3" fill="none" stroke="#fff" stroke-width="2"/></svg>
    <span>418 <span class="hl">Meadow Ln Braxton</span>, NC 28199</span>
  </div>
  <div class="abs contact c-web">
    <svg width="32" height="32" viewBox="0 0 32 32" aria-hidden="true"><circle cx="16" cy="16" r="14" fill="none" stroke="#fff" stroke-width="3"/><ellipse cx="16" cy="16" rx="6" ry="14" fill="none" stroke="#fff" stroke-width="2"/><line x1="2" y1="16" x2="30" y2="16" stroke="#fff" stroke-width="2"/></svg>
    <span>www.<span class="hl">MyBraxtonYard</span>.com</span>
  </div>
  <div class="abs contact c-mail">
    <svg width="32" height="32" viewBox="0 0 32 32" aria-hidden="true"><circle cx="16" cy="16" r="15" fill="#fff"/><rect x="8" y="10" width="16" height="12" rx="1" fill="none" stroke="var(--brown)" stroke-width="2"/><path d="M8 11 l8 6 l8 -6" fill="none" stroke="var(--brown)" stroke-width="2"/></svg>
    <span>office@<span class="hl">mybraxtonyard</span>.com</span>
  </div>

</main>
</body>
</html>
```